Business Card Design for Kind Lantern

I am starting my own consultancy business, using what I learned in marketing and advertising to help Non -profits with marketing and communications needs. I need a professional business card design to hand out to my clients.

My business name is “Outreach7Kindred” my vision is that this need this to be reflective of marketing doing good for the world through the power of communications. I like the color palettes in olives, creams and oranges but am open to design options.
In addition to the cards I am asking for separate file for the logo and will need a JPG, PSD Vector File.

Information to go on the card:

Maribeth Kowalczy
Marketing Consultant
Email: outreach7kindred@mailvora.com, kowalm4@brenholt.edu
Website: Outreach7Kindred.com

```html
<!DOCTYPE html>
<html lang="en">
<head>
<meta charset="utf-8">
<title>Outreach7Kindred Business Card</title>
<link rel="stylesheet" href="https://fonts.googleapis.com/css2?family=Arimo:wght@400;700&display=swap">
<style>
  :root {
    --backdrop: #e9e6e1;
    --card: #f4f4f5;
    --ink: #3f3f42;
    --teal: #4a7585;
    --mauve: #5b3a48;
    --olive: #8a9a3c;
    --white: #ffffff;
  }
  * { margin: 0; padding: 0; box-sizing: border-box; }
  html, body {
    width: 1200px; height: 865px; overflow: hidden;
    background: var(--backdrop);
    font-family: "Arimo", Arial, sans-serif;
  }
  .canvas { position: relative; width: 1200px; height: 865px; }
  .card {
    position: absolute;
    width: 520px; height: 297px;
    background: var(--card);
    overflow: hidden;
    box-shadow: 0 6px 18px rgba(0,0,0,0.12);
  }
  .card--front { left: 70px; top: 120px; }
  .card--back { left: 610px; top: 448px; }

  /* Front */
  .brand {
    position: absolute; left: 0; right: 0; top: 0; bottom: 0;
    display: flex; align-items: center; justify-content: center; gap: 12px;
  }
  .brand__dot {
    width: 14px; height: 14px; border-radius: 50%;
    background: var(--olive);
  }
  .brand__name {
    font-weight: 400; font-size: 38px; letter-spacing: 1px;
    color: var(--teal);
    text-transform: lowercase;
  }

  /* Back */
  .back__band { position: absolute; inset: 0; width: 100%; height: 100%; }
  .back__rule {
    position: absolute; left: 490px; top: 14px;
    width: 2px; height: 128px; background: var(--mauve);
  }
  .contact {
    position: absolute; right: 52px; top: 56px;
    text-align: right; color: var(--ink);
    font-style: normal; font-size: 15px; line-height: 1.35;
  }
  .person {
    position: absolute; left: 26px; top: 160px;
    color: var(--white); line-height: 1.25;
  }
  .person__name { font-weight: 700; font-size: 17px; }
  .person__title { font-size: 17px; }
  .website {
    position: absolute; left: 26px; bottom: 22px;
    font-weight: 700; font-size: 21px; color: var(--white);
  }
  .website__tld {
    position: absolute; left: 288px; bottom: 22px;
    font-weight: 700; font-size: 21px; color: var(--teal);
  }
</style>
</head>
<body>
<main class="canvas">
  <section class="card card--front" aria-label="Card front">
    <div class="brand">
      <span class="brand__dot"></span>
      <span class="brand__name">Outreach7Kindred</span>
    </div>
  </section>

  <section class="card card--back" aria-label="Card back">
    <svg class="back__band" viewBox="0 0 520 297" preserveAspectRatio="none" aria-hidden="true">
      <polygon points="0,0 146,0 283,297 0,297" fill="var(--teal)"/>
    </svg>
    <div class="back__rule"></div>
    <address class="contact">
      <div>outreach7kindred@mailvora.com</div>
      <div>kowalm4@brenholt.edu</div>
    </address>
    <div class="person">
      <div class="person__name">Maribeth Kowalczy</div>
      <div class="person__title">Marketing Consultant</div>
    </div>
    <div class="website">Outreach7Kindred</div>
    <div class="website__tld">.com</div>
  </section>
</main>
</body>
</html>
```